Business Card Design for an Investment Company

We need a business card design for our private investment company, called Ashbourne Partners. Ashbourne Partners is an investments partnership that aims to acquire shares in listed companies with a view to influencing those companies through active dialogue in order to improve their value. We need designs that use the logo colors (blue, grey, white), we need both English and Arabic on the business cards (can be on one side or 2 sides). The final logo should communicate professionalism, conservatism (nothing too fancy or too cheesy), that we are smart, conservative and old school.

Target Market(s)

Investment companies

Industry/Entity Type

Investment

Contact Information for Business Card

Khalid Yousef Rumaithi
Senior Executive Officer

Palm Terrace 07, Level 3, Office 215/12
HLMZ

+9714987650
krumaithi@ashbournepartners.com
www.ashbournepartners.com

Requirements
Must have
• Logo to be placed on the left hand side of the business card
• for the Arabic, we only need to have the name and title so it can be accomodated on one side so we can have the other side with full color and logo. The arabic that needs to be used is the below:
• خالد يوسف الرميثي
• المدير التنفيدي

```html
<!DOCTYPE html>
<html lang="en">
<head>
<meta charset="utf-8">
<title>Ashbourne Partners — Business Cards</title>
<link href="https://fonts.googleapis.com/css2?family=Montserrat:wght@400;500;700&family=Cairo:wght@400;700&display=swap" rel="stylesheet">
<style>
  :root {
    --stage-top: #2c2c2c;
    --stage-bottom: #0b0b0b;
    --slate: #646a73;
    --steel-blue: #3d6f9a;
    --brand-blue: #1f6aa5;
    --ink-grey: #4a4a4a;
    --paper: #ffffff;
  }
  * { box-sizing: border-box; margin: 0; padding: 0; }
  html, body { width: 1200px; height: 1200px; overflow: hidden; }
  body {
    background: linear-gradient(180deg, var(--stage-top), var(--stage-bottom));
    font-family: "Montserrat", sans-serif;
    display: flex;
    flex-direction: column;
    align-items: center;
    justify-content: center;
    gap: 64px;
  }
  .card {
    position: relative;
    width: 820px;
    height: 468px;
    border-radius: 40px;
    overflow: hidden;
    box-shadow: 0 24px 50px rgba(0,0,0,0.55);
  }
  .card--dark {
    background: linear-gradient(105deg, var(--slate) 0%, var(--steel-blue) 100%);
    color: var(--paper);
    --accent: var(--paper);
    --rule: rgba(255,255,255,0.7);
    --sub: var(--paper);
  }
  .card--light {
    background: var(--paper);
    color: var(--ink-grey);
    --accent: var(--brand-blue);
    --rule: var(--brand-blue);
    --sub: var(--ink-grey);
  }
  .brand-name {
    position: absolute;
    left: 64px;
    top: 112px;
    font-weight: 700;
    font-size: 54px;
    line-height: 1.2;
    letter-spacing: -1px;
    color: var(--accent);
    white-space: nowrap;
  }
  .arabic-block {
    position: absolute;
    right: 56px;
    top: 192px;
    direction: rtl;
    text-align: right;
    font-family: "Cairo", sans-serif;
    line-height: 1.3;
  }
  .arabic-name { font-weight: 700; font-size: 24px; color: var(--accent); }
  .arabic-role { font-size: 18px; color: var(--sub); }
  .divider {
    position: absolute;
    left: 330px;
    right: 0;
    top: 300px;
    height: 1px;
    background: var(--rule);
  }
  .holder {
    position: absolute;
    left: 64px;
    top: 248px;
    white-space: nowrap;
  }
  .holder-name {
    font-weight: 700;
    font-size: 28px;
    line-height: 1.1;
    color: var(--accent);
    letter-spacing: -0.5px;
  }
  .holder-role {
    font-size: 17px;
    color: var(--sub);
    margin-top: 4px;
  }
  .contacts {
    position: absolute;
    left: 64px;
    top: 340px;
    list-style: none;
    font-size: 16px;
    line-height: 27px;
    color: var(--sub);
    white-space: nowrap;
  }
  .contacts li { display: flex; align-items: center; gap: 12px; }
  .contacts svg { width: 19px; height: 19px; flex: none; }
  .contacts svg * { fill: var(--accent); }
  .address {
    position: absolute;
    right: 56px;
    top: 326px;
    text-align: right;
    font-size: 15px;
    line-height: 26px;
    color: var(--sub);
    white-space: nowrap;
  }
  .address-line { display: flex; justify-content: flex-end; align-items: center; gap: 10px; }
  .address svg { width: 14px; height: 18px; }
  .address svg path { fill: var(--accent); }
  .address .address-line--second { padding-right: 24px; }
</style>
</head>
<body>

<section class="card card--dark">
  <div class="brand-name">Ashbourne Partners</div>
  <div class="divider"></div>
  <div class="holder">
    <div class="holder-name">KHALID YOUSEF RUMAITHI</div>
    <div class="holder-role">Senior Executive Officer</div>
  </div>
  <ul class="contacts">
    <li><svg viewBox="0 0 20 20"><path d="M2 7c0-3 4-4 8-4s8 1 8 4v2h-4V7H6v2H2z"/><path d="M5 10h10l2 7H3z"/></svg>+9714987650</li>
    <li><svg viewBox="0 0 20 20"><path d="M10 1a9 9 0 1 0 0 18a9 9 0 0 0 0-18zm0 2c1 1.4 1.7 3.2 1.9 6H8.1c.2-2.8.9-4.6 1.9-6zM3.1 9a7 7 0 0 1 3.5-5.1C6.3 5 6.1 7 6 9zm0 2H6c.1 2 .3 4 .6 5.1A7 7 0 0 1 3.1 11zm5 0h3.8c-.2 2.8-.9 4.6-1.9 6-1-1.4-1.7-3.2-1.9-6zm5.9 0h2.9a7 7 0 0 1-3.5 5.1c.3-1.1.5-3.1.6-5.1zm0-2c-.1-2-.3-4-.6-5.1A7 7 0 0 1 16.9 9z"/></svg>www.ashbournepartners.com</li>
    <li><svg viewBox="0 0 20 20"><rect x="1" y="4" width="18" height="12"/></svg>krumaithi@ashbournepartners.com</li>
  </ul>
  <div class="address">
    <div class="address-line">Palm Terrace 07, Level 3, Office 215/12 <svg viewBox="0 0 14 18"><path d="M7 0a7 7 0 0 0-7 7c0 5 7 11 7 11s7-6 7-11a7 7 0 0 0-7-7zm0 4.5a2.5 2.5 0 1 1 0 5a2.5 2.5 0 0 1 0-5z"/></svg></div>
    <div class="address-line address-line--second">HLMZ</div>
  </div>
</section>

<section class="card card--light">
  <div class="brand-name">Ashbourne Partners</div>
  <div class="arabic-block" lang="ar">
    <div class="arabic-name">خالد يوسف الرميثي</div>
    <div class="arabic-role">المدير التنفيدي</div>
  </div>
  <div class="divider"></div>
  <div class="holder">
    <div class="holder-name">KHALID YOUSEF RUMAITHI</div>
    <div class="holder-role">Senior Executive Officer</div>
  </div>
  <ul class="contacts">
    <li><svg viewBox="0 0 20 20"><path d="M2 7c0-3 4-4 8-4s8 1 8 4v2h-4V7H6v2H2z"/><path d="M5 10h10l2 7H3z"/></svg>+9714987650</li>
    <li><svg viewBox="0 0 20 20"><path d="M10 1a9 9 0 1 0 0 18a9 9 0 0 0 0-18zm0 2c1 1.4 1.7 3.2 1.9 6H8.1c.2-2.8.9-4.6 1.9-6zM3.1 9a7 7 0 0 1 3.5-5.1C6.3 5 6.1 7 6 9zm0 2H6c.1 2 .3 4 .6 5.1A7 7 0 0 1 3.1 11zm5 0h3.8c-.2 2.8-.9 4.6-1.9 6-1-1.4-1.7-3.2-1.9-6zm5.9 0h2.9a7 7 0 0 1-3.5 5.1c.3-1.1.5-3.1.6-5.1zm0-2c-.1-2-.3-4-.6-5.1A7 7 0 0 1 16.9 9z"/></svg>www.ashbournepartners.com</li>
    <li><svg viewBox="0 0 20 20"><rect x="1" y="4" width="18" height="12"/></svg>krumaithi@ashbournepartners.com</li>
  </ul>
  <div class="address">
    <div class="address-line">Palm Terrace 07, Level 3, Office 215/12 <svg viewBox="0 0 14 18"><path d="M7 0a7 7 0 0 0-7 7c0 5 7 11 7 11s7-6 7-11a7 7 0 0 0-7-7zm0 4.5a2.5 2.5 0 1 1 0 5a2.5 2.5 0 0 1 0-5z"/></svg></div>
    <div class="address-line address-line--second">HLMZ</div>
  </div>
</section>

</body>
</html>
```